Harlowe Wine Label - Design a front and smaller back label for an exclusive red wine

Harlowe Wines produces a very high quality, high priced wine from an old and prestigous vineyard in one of Australia's oldest, but smallest wine growing regions. The grapevines are old (like old men with gnarled arms and trunks) and they produce fewer grapes than younger vines but the grape quality (and thus wine quality) is magnificent and highly sought after as it produces wine of exceptional quality.
The vineyard was purchased by the Harlowe family in February 2010 from a multinational wine company who made wonderful, trophy winning wines for 10 years before the vineyard went into a decline.
The challenge is to produce 2 labels - a simple main front label that focuses on the Harlowe brand and a smaller, information rich, back label that relates the history of the vineyard.
The labels should have a white or charcoal grey background and impart tradition, quality, exclusivity and a little self indulgence which is why we want the family crest incorporated - the choice of font will help.
It might also impart a sense of fun so that it appeals to the 25-35 year old age bracket.
The label should be kept clean and simple not loud and busy. Preferred colours are black, grey and white. Red is fine if used sparingly

Here are the details:_

Front Label (115 long x 65-90mm wide)

Harlowe
Lanternman’s Reserve
2011
Mudgee
Wine of Australia 750ml

Back Label (dimensions to suit text and front label design; font size small; text in black so that it is readable in less than optimal light (eg candlelight at a restaurant table).

Harlowe
Lanternman’s Reserve 2011

This is the first release of The Lanternman’s Reserve – just 100 dozen bottles were made. The wine was made from Shiraz and 10% Cabernet Sauvignon grapes sourced from an iconic Mudgee vineyard that was established 1966 by Peter Wyld. In 1994, the vineyard known as ”Copper Hollow”, became the source of a decade of formidable, trophy winning wines under Bellgrove’s and later Tinsley’s ownership. The 20ha vineyard was purchased by Marnie & Colette Harlowe in 2010. The Copper Hollow name was retained by Tinsleys; no wine has been released under this label since the 2006 vintage.

The shaky old Shiraz vines are slowly being restored to full health using careful cane pruning techniques that stimulates fresh, new tissue growth, more even bunch sizes and better grape quality and consistency. The Shiraz grapes used in this wine were hand-picked from two rows of the first crop from the 46 year old, cane pruned vines. The 2011 Reserve is the first step to re-establish the traditions of a famous vineyard and one of Australia’s most sought after export wines.

“Deep and intense purple hues with aromas of ripe blackberry fruits, spice and eucalypt with rich chocolate complemented by subtle oak overtones. A rich and full bodied wine exhibiting a soft yet generous palate with plum, forest fruits and mint chocolate notes. A fine grained tannin structure displaying integrated oak characters adds to the complexity of the wine. This wine was aged for 18 months in a blend of new French oak hogsheads and one year old American hogsheads, crafting a blend with great structure and length of flavour which will develop into a Mudgee classic” – Owen Parrish, Winemaker

13.5% Alc/Vol.
Contains approx 8.0 std drinks
Preservative (220) added

Harlowe Wines
Fernbrook Rd, Mudgee 2850
www.harlowewines-example.com.au
Updates

Project Deadline Extended
Reason: My apologies to the designers who have kindly submitted some wonderful designs. I am trying to achieve a conscentious between shareholders. This is difficult as they are in different parts of the world and I have learned through this experience that opinions on wine labels are quite diverse!!! The feedback I have received so far indicates the following (1) A light or white background is preferred (2) The crest should not be a dominant part of the label (3) The label needs to be clean, fresh and uncomplicated (4) If red is used it should be in minor detail only (5) "Harlowe" should be distinctive. The font is difficult for us! (6) We are considering "The Lanternman" RESERVE instead of "Lanternman's" RESERVE (7) The text on the back label is too long; I will edit and re-upload Many thanks for your help and patience Kind regards Marnie

Good Morning All,
I have edited the back label text to reduce the size of the label. A Word file with the changes has just been uploaded.
Cheers
Marnie

Dear Designers,
Thank you all so very much for the wonderful selection of designs you have submitted my family have all been overwhelmed by the quality and skill level exhibited and we all appreciate you your efforts
Kindest regards
Marnie

Target Market(s)

25-35 year old men and women of Australia, China, US & UK

Industry/Entity Type

Restaurant

Requirements
Must have
• Crest
Should not have
• Animals on the label

```html
<!DOCTYPE html>
<html lang="en">
<head>
<meta charset="utf-8">
<title>Harlowe – Lanternman’s Reserve Labels</title>
<link href="https://fonts.googleapis.com/css2?family=Old+Standard+TT:wght@400;700&family=Arimo:wght@400;700&display=swap" rel="stylesheet">
<style>
  :root {
    --ink: #111111;
    --paper: #ffffff;
    --backdrop: #ffffff;
    --rule: #444444;
    --sketch-light: #f1f1f1;
    --sketch-mid: #bdbdbd;
    --sketch-dark: #7a7a7a;
  }
  * { margin: 0; padding: 0; box-sizing: border-box; }
  html, body { width: 1200px; height: 900px; overflow: hidden; background: var(--backdrop); }
  .canvas { position: relative; width: 1200px; height: 900px; }

  .front-label {
    position: absolute; left: 160px; top: 40px; width: 318px; height: 408px;
    background: var(--paper); border: 1px solid var(--rule); overflow: hidden;
  }
  .reserve-band {
    height: 20px; background: var(--ink); color: var(--paper);
    font-family: "Arimo", Arial, sans-serif; font-size: 14px; letter-spacing: 1.2px;
    text-align: center; line-height: 20px; text-transform: uppercase;
  }
  .crest-mark {
    position: absolute; left: 50%; top: 52px; transform: translateX(-50%);
    display: flex; flex-direction: column; align-items: center; gap: 4px;
    font-family: "Old Standard TT", Georgia, serif; font-size: 9px; color: var(--ink);
  }
  .crest-mark .crest-square { width: 30px; height: 30px; border: 1px solid var(--ink); }
  .brand-name {
    position: absolute; font-family: "Old Standard TT", Georgia, serif; color: var(--ink);
    transform-origin: left top; transform: scale(0.78, 1.25); white-space: nowrap; line-height: 1;
  }
  .front-label .brand-name { left: 20px; top: 138px; font-size: 64px; }
  .vineyard-sketch {
    position: absolute; left: 6px; top: 208px; width: 302px; height: 196px;
    background: radial-gradient(ellipse at 75% 25%, var(--sketch-mid), transparent 45%),
                linear-gradient(170deg, var(--sketch-light) 0%, var(--sketch-mid) 55%, var(--sketch-dark) 100%);
    opacity: 0.75;
  }
  .vintage {
    position: absolute; right: 26px; top: 346px; text-align: right;
    font-family: "Arimo", Arial, sans-serif; font-weight: 700; color: var(--ink); line-height: 1;
  }
  .vintage .year { font-size: 27px; letter-spacing: 0.5px; }
  .vintage .region { font-size: 14px; margin-top: 2px; }
  .origin-volume {
    position: absolute; left: 8px; top: 402px; transform-origin: left top; transform: rotate(-90deg);
    font-family: "Arimo", Arial, sans-serif; font-size: 9px; color: var(--ink); white-space: nowrap;
  }

  .back-label {
    position: absolute; left: 180px; top: 467px; width: 298px; height: 390px;
    background: var(--paper); border: 1px solid var(--rule); padding: 24px 14px 10px;
    font-family: "Arimo", Arial, sans-serif; color: var(--ink);
    display: flex; flex-direction: column; overflow: hidden;
  }
  .back-heading { text-align: center; height: 64px; position: relative; flex: none; }
  .back-heading .brand-name {
    position: relative; display: inline-block; font-size: 40px;
    transform: scale(0.8, 1.2); transform-origin: center top;
  }
  .back-heading .reserve-title { position: absolute; left: 0; right: 0; top: 52px; font-size: 9.5px; font-weight: 700; }
  .story p { font-size: 7.9px; line-height: 10.4px; text-align: justify; margin-bottom: 8px; }
  .story p:last-child { margin-bottom: 0; }
  .back-details {
    display: flex; justify-content: space-between; font-size: 7.9px; line-height: 10.4px;
    margin-top: auto; flex: none;
  }
  .back-details .winery { text-align: right; }
</style>
</head>
<body>
<main class="canvas">
  <section class="front-label" aria-label="Front label">
    <div class="reserve-band">Lanternman’s Reserve</div>
    <div class="crest-mark"><span class="crest-square"></span><span>Harlowe</span></div>
    <h1 class="brand-name">Harlowe</h1>
    <div class="vineyard-sketch" role="img" aria-label="Pencil sketch of rolling vineyard rows with a tree on the hill"></div>
    <div class="vintage"><div class="year">2011</div><div class="region">Mudgee</div></div>
    <div class="origin-volume">Wine of Australia  750ml</div>
  </section>

  <section class="back-label" aria-label="Back label">
    <header class="back-heading">
      <h2 class="brand-name">Harlowe</h2>
      <div class="reserve-title">Lanternman’s Reserve</div>
    </header>
    <div class="story">
      <p>This is the first release of the Lanternman’s Reserve – just 100 dozen bottles were made. The wine was made from Shiraz and 10% Cabernet Sauvignon grapes sourced from an iconic Mudgee vineyard that was established 1966 by Peter Wyld. In 1994, the vineyard known as “Copper Hollow” became the source of a decade of formidable, trophy winning wines under Bellgrove’s and later Tinsley’s ownership. The 20ha vineyard was purchased by Marnie &amp; Colette Harlowe in 2010. The Copper Hollow name was retained by Tinsleys; no wine has been released under this label since the 2006 vintage.</p>
      <p>The shaky old Shiraz vines are slowly being restored to full health using careful cane pruning techniques that stimulates fresh, new tissue growth, more even bunch sizes and better grape quality and consistency. The Shiraz grapes used in this wine were hand-picked from two rows of the first crop from the 46 year old, cane pruned vines. The 2011 Reserve is the first step to re-establish the traditions of a famous vineyard and one of Australia’s most sought after export wines.</p>
      <p>“Deep and intense purple hues with aromas of ripe blackberry fruits, spice and eucalypt with rich chocolate complemented by subtle oak overtones. A rich and full bodied wine exhibiting a soft yet generous palate with plum, forest fruits and mint chocolate notes. A fine grained tannin structure displaying integrated oak characters adds to the complexity of the wine. This wine was aged for 18 months in a blend of new French oak hogsheads and one year old American hogsheads, crafting a blend with great structure and length of flavour which will develop into a Mudgee classic” – Owen Parrish, Winemaker</p>
    </div>
    <footer class="back-details">
      <div class="compliance">13.5% Alc/Vol.<br>Contains approx 8.0 std drinks<br>Preservative (220) added</div>
      <div class="winery">Harlowe Wines<br>Fernbrook Rd, Mudgee 2850<br>www.harlowewines-example.com.au</div>
    </footer>
  </section>
</main>
</body>
</html>
```